Generator Control - Superyacht Power Management System

We need a graphic design for a Touch Screen interface to control generators on Superyachts. We have a layout of the control system worked out, but need nice graphics to go with it.
The graphics comes down to a 300x460px App that i replicate several times on my 15" touchscreen as required.
See attached images.
The interface is divided up into 4 sections:
• Section#1 - 4 rectangles for the control
• Section#2 - a vertical bar graph,
• Section#3 - a section to display custom information
• Section#4 - a circuit breaker symbol.
The dimensions in pixels must be as per the attached image.
SECTION#1:
The 4 control rectangles correspond to 4 control modes:
• STOP – colours based on RED
• RUN – colours based on ORANGE
• RUN ONLINE – colours based on GREEN
• AUTO – colours based on BLUE
• THE TEXT DOESN’T HAVE TO BE ON THE GRAPHICS, WE JUST NEED THE BACKGROUND FOR THE TEXT, I ADD THE TEXT LATER USING SOFTWARE.
Each control rectangle needs to have 3 clearly identifiable states:
• Active/Selected (this is the currently active mode)
• Not Active/Not Selected (this mode is available but not currently active)
• Unavailable (this mode is not available)
SECTION#2:
The vertical bar graph design only needs the outline/frame of the bar graph. The actual moving part can be left blank; I will add that in later using an animation.
SECTION#3:
Free to look good as you want. See attached image for reference.
Within section#3 (at the top) is a 40x240px subsection, and should simply by 2 states, green or 'background colour of section#3 '. (green for when the generator is running, blend with the rest of section#3 when it is not). There are about 10 different texts I add on top of that square using software, corresponding to the status of the generator (starting, deloading, synchronizing, etc.)
SECTION#4:
Graphical representation of an electrical switch. Can be in two positions: opened or closed. See attached image as reference.

Cheif Engineers /Captains on Superyachts

Graphic Design

• Must have the same graphics style as the uploaded file#2

```html
<!DOCTYPE html>
<html lang="en">
<head>
<meta charset="utf-8">
<title>Starboard Generator Control</title>
<link rel="stylesheet" href="https://fonts.googleapis.com/css2?family=Noto+Sans:wght@400;700&display=swap">
<style>
  :root {
    --bg: #000000;
    --bus-line: #262c48;
    --panel-bg: #0c1020;
    --panel-border: #3a3f4c;
    --header-grey-light: #a8a8a8;
    --header-grey-dark: #4a4a4a;
    --header-status: #1b2914;
    --text-main: #f2f2f2;
    --text-label: #e6e6e6;
    --field-border: #b4b6ec;
    --field-bg: #05060c;
    --online-top: #5cae6c;
    --online-bottom: #2f7c42;
    --online-ring: #c0c6ff;
    --run-off: #35261a;
    --run-off-text: #6c5a48;
    --stop-off: #3f1717;
    --stop-off-text: #6e4444;
    --auto-top: #3038c8;
    --auto-bottom: #0c0c96;
    --auto-border: #6f74e8;
    --bar-frame: #2a2e38;
    --bar-track: #151820;
    --bar-strip: #8c9098;
    --seg-off: #101216;
    --seg-off-edge: #3a3e46;
    --seg-on-top: #a8bc5c;
    --seg-on-bottom: #5e7230;
  }
  * { box-sizing: border-box; margin: 0; padding: 0; }
  html, body {
    width: 876px; height: 1200px; overflow: hidden;
    background: var(--bg);
    font-family: "Noto Sans", Verdana, sans-serif;
  }
  .stage {
    position: absolute; left: 0; top: 0;
    width: 330px; height: 452px;
    transform: scale(2.6545);
    transform-origin: 0 0;
  }
  .breaker { position: absolute; left: 0; top: 0; }

  .generator-panel {
    position: absolute; left: 12px; top: 68px;
    width: 306px; height: 358px;
    background: var(--panel-bg);
    border: 2px solid var(--panel-border);
    border-radius: 6px;
    overflow: hidden;
  }
  .panel-header {
    position: absolute; left: 0; top: 0; width: 100%; height: 20px;
    background: var(--header-status);
    color: var(--text-main); font-size: 10.5px; line-height: 20px;
  }
  .panel-header .title-tab {
    position: absolute; left: 0; top: 0; height: 20px; width: 160px;
    background: linear-gradient(180deg, var(--header-grey-light), var(--header-grey-dark));
    border-top-right-radius: 18px 20px;
    padding-left: 6px;
  }
  .panel-header .status { position: absolute; right: 6px; top: 0; }

  .mode-button {
    position: absolute; width: 105px; height: 66px;
    border-radius: 6px;
    display: flex; align-items: center; justify-content: center;
    font-size: 14px;
  }
  .mode-online-active {
    left: 6px; top: 34px;
    background: linear-gradient(180deg, var(--online-top), var(--online-bottom));
    border: 2px solid var(--online-ring);
    box-shadow: 0 0 4px var(--online-ring);
    color: #fff; font-weight: 700;
  }
  .mode-run-unavailable {
    left: 121px; top: 34px;
    background: var(--run-off); color: var(--run-off-text);
  }
  .mode-stop-unavailable {
    left: 6px; top: 110px;
    background: var(--stop-off); color: var(--stop-off-text);
  }
  .mode-auto-available {
    left: 121px; top: 110px;
    background: linear-gradient(180deg, var(--auto-top), var(--auto-bottom));
    border: 1px solid var(--auto-border);
    color: #fff;
  }

  .readout {
    position: absolute; height: 27px;
    border: 2px solid var(--field-border); border-radius: 4px;
    background: var(--field-bg); color: #fff;
    display: flex; align-items: center; justify-content: center;
    font-size: 15px;
  }
  .readout.small { height: 26px; width: 27px; font-size: 8.5px; }
  .readout.clock { font-size: 8.5px; }
  .readout-label {
    position: absolute; color: var(--text-label); font-size: 10.5px; line-height: 12px;
  }
  .readout-label.under { font-size: 8px; width: 27px; text-align: center; }

  .load-meter .frame {
    position: absolute; left: 244px; top: 55px; width: 42px; height: 268px;
    background: var(--bar-track);
    border: 2px solid var(--bar-frame); border-radius: 4px;
  }
  .load-meter .strip {
    position: absolute; left: 262px; top: 57px; width: 6px; height: 264px;
    background: linear-gradient(90deg, transparent, var(--bar-strip), transparent);
  }
  .load-meter .segment {
    position: absolute; left: 251px; width: 28px; height: 19px;
    border-radius: 5px;
    background: var(--seg-off); border: 1px solid var(--seg-off-edge);
    opacity: .9;
  }
  .load-meter .segment.on {
    background: linear-gradient(180deg, var(--seg-on-top), var(--seg-on-bottom));
    border-color: var(--seg-on-bottom);
  }
  .load-meter .segment.half {
    background: linear-gradient(180deg, var(--seg-off) 45%, var(--seg-on-top) 46%, var(--seg-on-bottom));
  }
</style>
</head>
<body>
<div class="stage">
  <svg class="breaker" width="330" height="70" viewBox="0 0 330 70" aria-label="Circuit breaker, closed">
    <line x1="0" y1="10" x2="330" y2="10" stroke="#262c48" stroke-width="3"/>
    <line x1="155" y1="0" x2="155" y2="22" stroke="#262c48" stroke-width="2"/>
    <circle cx="155" cy="28" r="6" fill="none" stroke="#262c48" stroke-width="2"/>
    <line x1="155" y1="34" x2="155" y2="70" stroke="#262c48" stroke-width="2"/>
  </svg>

  <section class="generator-panel">
    <header class="panel-header">
      <span class="title-tab">Starboard Generator</span>
      <span class="status">Status: Running Online</span>
    </header>

    <div class="mode-button mode-online-active">Run Online</div>
    <div class="mode-button mode-run-unavailable">Run Online</div>
    <div class="mode-button mode-stop-unavailable">Run</div>
    <div class="mode-button mode-auto-available">Automatic</div>

    <div class="readout" style="left:6px;top:190px;width:38px">85</div>
    <div class="readout-label" style="left:62px;top:192px">Water<br>Temp.</div>
    <div class="readout" style="left:6px;top:233px;width:38px">3.8</div>
    <div class="readout-label" style="left:62px;top:235px">Oil<br>Pres.</div>
    <div class="readout" style="left:6px;top:277px;width:48px">1500</div>
    <div class="readout-label" style="left:62px;top:285px">RPM</div>
    <div class="readout clock" style="left:6px;top:318px;width:50px;height:30px">00:03:33</div>
    <div class="readout-label" style="left:62px;top:320px">Online<br>Time</div>

    <div class="readout small" style="left:122px;top:189px">230</div>
    <div class="readout small" style="left:159px;top:189px">400</div>
    <div class="readout small" style="left:196px;top:189px">50.0</div>
    <div class="readout-label under" style="left:122px;top:219px">VAC</div>
    <div class="readout-label under" style="left:159px;top:219px">VAC</div>
    <div class="readout-label under" style="left:196px;top:219px">HZ</div>

    <div class="readout small" style="left:122px;top:250px">15</div>
    <div class="readout small" style="left:159px;top:250px">22</div>
    <div class="readout small" style="left:196px;top:250px">19</div>
    <div class="readout-label under" style="left:122px;top:282px">AL1</div>
    <div class="readout-label under" style="left:159px;top:282px">AL2</div>
    <div class="readout-label under" style="left:196px;top:282px">AL3</div>

    <div class="readout small" style="left:122px;top:311px">45</div>
    <div class="readout small" style="left:159px;top:311px">0.00</div>
    <div class="readout-label under" style="left:122px;top:342px">KVA</div>
    <div class="readout-label under" style="left:159px;top:342px">PF</div>

    <div class="load-meter">
      <div class="readout small" style="left:244px;top:26px;width:32px;height:22px;font-size:9px">63 %</div>
      <div class="frame"></div>
      <div class="segment" style="top:65px"></div>
      <div class="segment" style="top:90px"></div>
      <div class="segment" style="top:115px"></div>
      <div class="segment" style="top:140px"></div>
      <div class="segment" style="top:165px"></div>
      <div class="segment half" style="top:190px"></div>
      <div class="segment on" style="top:215px"></div>
      <div class="segment on" style="top:240px"></div>
      <div class="segment on" style="top:265px"></div>
      <div class="segment on" style="top:290px"></div>
      <div class="strip"></div>
      <div class="readout small" style="left:244px;top:323px;width:42px;height:30px;line-height:10px;flex-direction:column">41<span>KW</span></div>
    </div>
  </section>
</div>
</body>
</html>
```